PowerPoint Template Design for Cobalt Lending

Design a PowerPoint template for Cobalt Lending, tailored for presentations to sophisticated mortgage servicing investors. The template should reflect a high level of professionalism, with a clean and modern aesthetic that resonates with an informed and discerning audience. The design must effectively integrate Cobalt Lending's branding elements, ensuring a coherent visual narrative that reinforces our reputation for expertise and reliability in the mortgage servicing sector.

```html
<!DOCTYPE html>
<html lang="en">
<head>
<meta charset="utf-8">
<title>Cobalt Lending – Presentation Template</title>
<link rel="stylesheet" href="https://fonts.googleapis.com/css2?family=Roboto:wght@300;400;500;700;900&family=Montserrat:wght@800;900&display=swap">
<style>
:root{
  --gold:#e0b13c;
  --gold-pale:#f4dea4;
  --navy:#2e2b6e;
  --navy-card:#3a3f8a;
  --ink:#2b2a5c;
  --teal:#38b2ae;
  --text:#6b6b6b;
  --muted:#a8a8a8;
  --canvas:#e9edf0;
  --white:#ffffff;
}
*{box-sizing:border-box;margin:0;padding:0}
html,body{width:937px;height:1200px;overflow:hidden}
body{background:radial-gradient(ellipse at 50% 40%,#f2f5f7 0%,var(--canvas) 70%);font-family:'Roboto',Arial,sans-serif;color:var(--text);position:relative}
.slide{position:absolute;background:var(--white);overflow:hidden;box-shadow:0 6px 14px rgba(40,55,75,.18)}
.abs{position:absolute}
.photo{position:absolute}
.h-gold{color:var(--gold);font-weight:300;letter-spacing:.2px}
.center{text-align:center;left:0;right:0}
.tiny{font-size:3.2px;line-height:4.2px;color:var(--text)}
.small{font-size:4px;line-height:5.2px}
.brand{font-family:'Roboto',Arial,sans-serif;font-weight:700}

/* title slide */
.title-slide{left:329px;top:66px;width:280px;height:157px}
.title-slide .photo{inset:0;background:linear-gradient(180deg,#4f5c6a 0%,#7d8892 35%,#9aa0a2 55%,#3c6f80 72%,#4d6a3e 100%)}
.title-slide .brand{top:12px;font-size:12px;color:var(--gold)}
.title-slide .rule{left:37px;width:210px;height:.6px;background:rgba(255,255,255,.8)}
.title-slide h1{top:68px;font-size:14px;font-weight:700;color:var(--white);letter-spacing:.3px}

/* numbers */
.numbers{left:17px;top:189px;width:279px;height:157px}
.numbers .photo{left:0;top:0;width:100%;height:90px;background:linear-gradient(180deg,#2f3b46 0%,#5b4a3c 55%,#283322 100%)}
.numbers h2{top:31px;font-size:13px;font-weight:700;color:var(--white)}
.numbers .sub{top:51px;font-size:7.5px;color:#eee;font-weight:300}
.numbers .bar{top:64px;left:128px;width:22px;height:1.2px;background:var(--white)}
.stat{position:absolute;top:79px;width:60px;text-align:center}
.stat .dot{width:22px;height:22px;border-radius:50%;background:var(--gold);margin:0 auto;display:flex;align-items:center;justify-content:center}
.stat .lbl{font-size:4px;margin-top:5px;color:var(--text)}
.stat .num{font-size:13px;color:var(--gold);font-weight:500;margin-top:2px}

/* advantages */
.advantages{left:641px;top:189px;width:280px;height:157px;background:var(--navy)}
.advantages h2{top:21px;font-size:13px;font-weight:400;color:var(--white)}
.advantages .dash{top:44px;left:129px;width:22px;height:1.2px;background:var(--white)}
.adv-card{position:absolute;top:58px;width:46px;height:85px;background:var(--navy-card);border-top:3px solid var(--gold);text-align:center;padding:6px 3px 0;color:var(--white)}
.adv-card b{display:block;font-size:4px;margin:4px 0 3px}
.adv-card p{font-size:2.8px;line-height:3.8px;color:#dfe0f0}

/* company */
.company{left:329px;top:268px;width:280px;height:157px}
.company h2{left:21px;top:22px;font-size:11px;line-height:13px}
.company .para{left:21px;top:67px;width:92px;text-align:justify}
.company .more{left:21px;top:113px;width:33px;height:6px;border:.5px solid var(--gold);font-size:2.8px;color:var(--gold);text-align:center;line-height:5px}
.company .url{left:21px;top:126px;font-size:3.2px;color:var(--gold);display:flex;align-items:center;gap:3px}
.company .photo{left:168px;top:0;width:112px;height:157px;background:linear-gradient(180deg,#b9c7d4 0%,#8b8e8f 45%,#5f6a55 80%,#7b7b74 100%)}
.company .card{position:absolute;left:126px;top:20px;width:65px;height:116px;background:var(--white);box-shadow:0 2px 6px rgba(0,0,0,.15);text-align:center;padding:9px 5px 0}
.company .card b{display:block;font-size:3.6px;color:var(--gold);margin:4px 0 1px}
.company .card p{margin-bottom:4px}

/* numbered list */
.list{left:17px;top:379px;width:279px;height:166px}
.list h2{top:11px;font-size:12px}
.list .sub{top:29px;font-size:4px;color:var(--muted)}
.item{position:absolute;left:13px;display:flex;gap:5px;align-items:flex-start}
.item .n{width:13px;height:13px;border-radius:50%;background:var(--gold);color:var(--white);font-size:5px;font-weight:500;display:flex;align-items:center;justify-content:center;flex:none}
.item b{display:block;font-size:4.5px;color:var(--gold);font-weight:500;margin-bottom:2px}
.item p{font-size:3.3px;color:#444}

/* gold list with house */
.gold-list{left:329px;top:468px;width:280px;height:158px}
.gold-list .panel{position:absolute;left:0;top:0;width:140px;height:100%;background:var(--gold)}
.gold-list .photo{left:140px;top:0;width:140px;height:100%;background:linear-gradient(180deg,#a8c2dc 0%,#dde6ee 45%,#cfd2d4 65%,#5f6a5c 100%)}
.g-item{position:absolute;left:12px;display:flex;gap:4px;color:var(--white)}
.g-item .n{width:12px;height:12px;border-radius:50%;border:.7px solid var(--white);font-size:4.2px;display:flex;align-items:center;justify-content:center;flex:none}
.g-item b{display:block;font-size:4.2px;margin-bottom:1.5px}
.g-item p{font-size:3.2px;line-height:6px;width:90px}
.gold-list .hub{position:absolute;left:124px;top:64px;width:32px;height:32px;border-radius:50%;background:var(--white);display:flex;align-items:center;justify-content:center;box-shadow:0 1px 4px rgba(0,0,0,.2)}

/* interior */
.interior{left:641px;top:391px;width:279px;height:156px}
.interior .photo{left:0;top:0;width:104px;height:100%;background:linear-gradient(180deg,#e7e3dc 0%,#cfc6b8 45%,#a88f74 70%,#e8e2d8 100%)}
.interior .band{position:absolute;left:104px;top:0;width:16px;height:100%;background:var(--gold)}
.interior h2{left:132px;top:9px;font-size:12px}
.interior .para{left:132px;top:40px;width:132px}
.interior .col{position:absolute;top:84px;width:48px}
.interior .col b{display:block;font-size:3.8px;color:var(--gold);margin-bottom:4px}

/* team photo cards */
.duo{left:17px;top:591px;width:281px;height:158px}
.duo .photo{left:0;top:0;width:100%;height:66px;background:linear-gradient(180deg,#5a4c44 0%,#8a6f5c 50%,#c7b29a 100%)}
.duo-card{position:absolute;top:47px;width:105px;height:83px;background:var(--gold-pale);padding:0}
.duo-card .top{height:19px;background:rgba(224,177,60,.78);color:var(--white);font-size:5px;font-weight:700;padding:7px 0 0 11px}
.duo-card p{font-size:3.3px;line-height:4.2px;color:var(--white);padding:8px 11px 0}
.duo .foot{left:25px;top:137px;width:230px;font-size:4px;line-height:5px;color:var(--gold)}

/* services */
.services{left:329px;top:668px;width:279px;height:157px}
.services h2{top:10px;font-size:12px}
.services .sub{top:27px;font-size:3.6px;color:var(--muted)}
.services .stat-card{position:absolute;left:35px;top:46px;width:68px;height:97px;background:var(--gold);box-shadow:0 2px 5px rgba(0,0,0,.15);text-align:center;color:var(--white);padding-top:9px}
.services .stat-card .y{font-size:6px;font-weight:300}
.services .stat-card .y span{font-size:3.2px}
.services .stat-card .s{font-size:3.3px;margin-top:5px;line-height:4.2px;opacity:.9}
.services .arrow{position:absolute;left:98px;top:92px;width:7px;height:7px;border-radius:50%;background:var(--white);box-shadow:0 0 2px rgba(0,0,0,.2);font-size:4px;color:#3a9bd8;text-align:center;line-height:7px}
.srv{position:absolute;display:flex;gap:7px;align-items:center}
.srv .n{font-size:13px;color:var(--gold);font-weight:300}
.srv b{display:block;font-size:3.5px;color:var(--gold);margin-bottom:1px}
.srv p{font-size:2.8px;line-height:3.8px;width:80px}
.srv.boxed{left:130px;top:47px;width:114px;height:31px;background:var(--white);box-shadow:0 1px 5px rgba(0,0,0,.13);padding-left:7px}

/* meet team */
.team{left:642px;top:591px;width:280px;height:158px}
.team h2{top:8px;font-size:13px}
.team .sub{top:28px;font-size:4px;color:#777}
.member{position:absolute;top:45px;width:70px}
.member .frame{height:80px;position:relative}
.member .frame .g{position:absolute;left:0;right:0;top:28px;bottom:0;background:var(--gold)}
.member .frame .p{position:absolute;left:8px;top:0;width:54px;height:53px;background:#f1f1f1}
.member .name{position:absolute;left:0;right:0;top:62px;text-align:center;font-size:3.4px;color:var(--white)}
.member .pos{position:absolute;left:0;right:0;top:68px;text-align:center;font-size:4.6px;font-weight:700;color:var(--white)}
.member .social{display:flex;gap:2.5px;justify-content:center;margin-top:8px}
.member .social i{width:8px;height:8px;border:.6px solid var(--gold);border-radius:50%}

/* chart */
.chart{left:17px;top:786px;width:279px;height:159px}
.chart h2{top:10px;font-size:12px}
.chart .sub{top:27px;font-size:3.6px;color:var(--muted)}
.chart .foot-bar{left:0;top:145px;width:22px;height:3px;background:var(--gold)}
.chart .foot{left:25px;top:144px;font-size:3px;color:#666}
.chart .page{right:7px;top:149px;font-size:3px;color:#666}

/* table */
.table-slide{left:329px;top:868px;width:280px;height:157px}
.table-slide h2{top:10px;font-size:12px}
.table-slide .sub{top:27px;font-size:3.6px;color:var(--muted)}
.data{position:absolute;left:13px;top:49px;width:254px;border-collapse:collapse;font-size:3px;color:#666}
.data th{background:var(--gold);color:var(--white);font-weight:400;height:7.5px;border:.4px solid #f0c763}
.data td{height:7.7px;text-align:center;border-bottom:.3px solid #ececec}
.data td:first-child{text-align:left;padding-left:5px}
.data tr:nth-child(even) td{background:#f7f7f7}

/* break */
.break{left:642px;top:786px;width:279px;height:157px}
.break .photo{inset:0;background:linear-gradient(180deg,#3f4f5c 0%,#8a8f8c 40%,#6e6a5c 62%,#2f5a6a 82%,#233f46 100%)}
.break .line{position:absolute;left:94px;width:84px;height:1.2px;background:var(--gold)}
.break h2{top:65px;font-size:12.5px;font-weight:700;color:var(--gold)}

/* Q&A */
.qa{left:17px;top:985px;width:280px;height:157px}
.qa .map{left:40px;top:30px;width:200px;height:95px;background:radial-gradient(ellipse at center,#f3f4f6 0%,rgba(255,255,255,0) 70%)}
.qa .mark{top:33px;font-family:'Montserrat',Arial,sans-serif;font-weight:900;font-size:48px;color:var(--gold);letter-spacing:-2px;line-height:48px}
.qa .q{top:104px;font-size:7.5px;line-height:10px;color:var(--gold);font-weight:300}

/* contact */
.contact{left:642px;top:985px;width:279px;height:157px}
.contact .brand{top:12px;font-size:12px;color:var(--navy)}
.contact .row{position:absolute;left:12px;right:8px;top:44px;display:flex;justify-content:space-between;align-items:center;font-size:2.8px;color:var(--gold)}
.contact .row span{display:flex;align-items:center;gap:3px}
.contact .url{top:62px;font-size:4px;color:var(--gold)}
.contact .social{position:absolute;top:70px;left:0;right:0;display:flex;gap:3px;justify-content:center}
.contact .social i{width:10px;height:10px;border-radius:50%;background:var(--navy)}
.contact .photo{left:0;top:88px;width:100%;height:69px;background:linear-gradient(180deg,#e9eef2 0%,#d8d5cd 40%,#8a826f 75%,#4c5a45 100%)}
</style>
</head>
<body>

<!-- Title slide -->
<section class="slide title-slide">
  <div class="photo" role="img" aria-label="Photo of a modern white villa with a swimming pool at dusk"></div>
  <div class="abs center brand">Cobalt Lending</div>
  <div class="abs rule" style="top:64px"></div>
  <h1 class="abs center">TITLE OF&nbsp; THE PRESENTATION</h1>
  <div class="abs rule" style="top:87px"></div>
</section>

<!-- Numbers -->
<section class="slide numbers">
  <div class="photo" role="img" aria-label="Photo of a family house lit at sunset"></div>
  <h2 class="abs center">OUR AWESOME NUMBERS</h2>
  <div class="abs center sub">Counters Numbers Speak</div>
  <div class="abs bar"></div>
  <div class="stat" style="left:24px"><div class="dot"><svg width="11" height="11" viewBox="0 0 12 12"><path d="M2 9l6-6 2 2-6 6H2z" fill="none" stroke="#fff" stroke-width="1"/></svg></div><div class="lbl">Company Branches</div><div class="num">60</div></div>
  <div class="stat" style="left:80px"><div class="dot"><svg width="11" height="11" viewBox="0 0 12 12"><rect x="2" y="3" width="8" height="6" transform="rotate(-30 6 6)" fill="none" stroke="#fff" stroke-width="1"/></svg></div><div class="lbl">PROJECTS COMPLETED</div><div class="num">653</div></div>
  <div class="stat" style="left:137px"><div class="dot"><svg width="11" height="11" viewBox="0 0 12 12"><path d="M2 5h2l5-3v8L4 7H2z" fill="#fff"/></svg></div><div class="lbl">Happy clients</div><div class="num">894 K</div></div>
  <div class="stat" style="left:194px"><div class="dot"><svg width="11" height="11" viewBox="0 0 12 12"><path d="M1 5l5-2 5 2-5 2z M3 6v3h6V6" fill="none" stroke="#fff" stroke-width="1"/></svg></div><div class="lbl">Year Of Experience</div><div class="num">32</div></div>
</section>

<!-- Advantages -->
<section class="slide advantages">
  <h2 class="abs center">OUR ADVANTAGES</h2>
  <div class="abs dash"></div>
  <div class="adv-card" style="left:27px"><svg width="13" height="11" viewBox="0 0 13 11"><rect x=".5" y=".5" width="12" height="10" fill="none" stroke="#fff" stroke-width=".8"/><rect x="2.5" y="3" width="4" height="3" fill="none" stroke="#fff" stroke-width=".6"/><path d="M8 4h3M8 6h3M2.5 8h8" stroke="#fff" stroke-width=".6"/></svg><b>Insert title here</b><p>There are many variations of passages lorem ipsum available, but the majority</p><p style="margin-top:2px">There are many variations of passages lorem ipsum available, but the majority</p></div>
  <div class="adv-card" style="left:87px"><svg width="13" height="11" viewBox="0 0 13 11"><path d="M1 4h3l5-3v9L4 7H1z" fill="none" stroke="#fff" stroke-width=".8"/><path d="M10.5 3.5l2-1M10.5 5.5h2M10.5 7.5l2 1" stroke="#fff" stroke-width=".6"/></svg><b>Insert title here</b><p>There are many variations of passages lorem ipsum available, but the majority</p><p style="margin-top:2px">There are many variations of passages lorem ipsum available, but the majority</p></div>
  <div class="adv-card" style="left:146px"><svg width="13" height="11" viewBox="0 0 13 11"><circle cx="4" cy="3" r="2" fill="none" stroke="#fff" stroke-width=".7"/><circle cx="8.5" cy="3" r="2" fill="none" stroke="#fff" stroke-width=".7"/><rect x="2" y="5.5" width="7" height="4" fill="none" stroke="#fff" stroke-width=".7"/><path d="M9 7l3-1.5v4L9 8" fill="none" stroke="#fff" stroke-width=".7"/></svg><b>Insert title here</b><p>There are many variations of passages lorem ipsum available, but the majority</p><p style="margin-top:2px">There are many variations of passages lorem ipsum available, but the majority</p></div>
  <div class="adv-card" style="left:204px"><svg width="13" height="11" viewBox="0 0 13 11"><circle cx="6.5" cy="5.5" r="4.8" fill="none" stroke="#fff" stroke-width=".7"/><ellipse cx="6.5" cy="5.5" rx="2" ry="4.8" fill="none" stroke="#fff" stroke-width=".6"/><path d="M1.7 5.5h9.6M2.5 3h8M2.5 8h8" stroke="#fff" stroke-width=".5"/></svg><b>Insert title here</b><p>There are many variations of passages lorem ipsum available, but the majority</p><p style="margin-top:2px">There are many variations of passages lorem ipsum available, but the majority</p></div>
</section>

<!-- About company -->
<section class="slide company">
  <h2 class="abs h-gold">WHAT ABOUT<br>OUR<br>COMPANY</h2>
  <p class="abs tiny para">There are many variations of passages of lorem ipsum available, but the majority have suffered alteration in some form, by injected humour, or randomized words which don't look even slightly believable. If you are going to use a passage of lorem ipsum, you need to be sure there isn't anything embarrassing hidden in the middle of text.</p>
  <div class="abs more">Read more</div>
  <div class="abs url"><svg width="5" height="5" viewBox="0 0 10 10"><circle cx="5" cy="5" r="4.3" fill="none" stroke="#e0b13c" stroke-width="1"/><path d="M1 5h8M5 1v8" stroke="#e0b13c" stroke-width=".7"/></svg>https://www.cobaltlending.com/</div>
  <div class="photo" role="img" aria-label="Photo of modern apartment buildings"></div>
  <div class="card">
    <svg width="16" height="14" viewBox="0 0 16 14"><path d="M1 4L8 1l7 3z" fill="none" stroke="#e0b13c" stroke-width=".8"/><path d="M3 5v6M6 5v6M10 5v6M13 5v6M1 12h14M1 13.5h14" stroke="#e0b13c" stroke-width=".8"/></svg>
    <b>Insert title here</b>
    <p class="tiny">There are many variations of passages of lorem ipsum available, but the</p>
    <p class="tiny">There are many variations of passages of lorem ipsum available, but the</p>
    <p class="tiny" style="margin-top:8px">There are many variations of passages of lorem ipsum available, but the</p>
    <p class="tiny" style="margin-top:8px">There are many variations of passages of lorem ipsum available, but the</p>
  </div>
</section>

<!-- Numbered list -->
<section class="slide list">
  <h2 class="abs center h-gold">TITLE GOES HERE</h2>
  <div class="abs center sub">Enter your subhead line here</div>
  <div class="item" style="top:53px"><div class="n">01</div><div><b>TITLE GOES HERE</b><p>This is a sample text. You simply add your own text and description here. This text is fully editable.</p></div></div>
  <div class="item" style="top:80px"><div class="n">02</div><div><b>TITLE GOES HERE</b><p>This is a sample text. You simply add your own text and description here. This text is fully editable.</p></div></div>
  <div class="item" style="top:107px"><div class="n">03</div><div><b>TITLE GOES HERE</b><p>This is a sample text. You simply add your own text and description here. This text is fully editable.</p></div></div>
  <div class="item" style="top:134px"><div class="n">04</div><div><b>TITLE GOES HERE</b><p>This is a sample text. You simply add your own text and description here. This text is fully editable.</p></div></div>
</section>

<!-- Gold list with house -->
<section class="slide gold-list">
  <div class="panel"></div>
  <div class="photo" role="img" aria-label="Photo of a modern two-storey house under a cloudy sky"></div>
  <div class="g-item" style="top:31px"><div class="n">01</div><div><b>TITLE GOES HERE</b><p>This is a sample text. You simply add your own text and description here. This text is fully editable.</p></div></div>
  <div class="g-item" style="top:57px"><div class="n">02</div><div><b>TITLE GOES HERE</b><p>This is a sample text. You simply add your own text and description here. This text is fully editable.</p></div></div>
  <div class="g-item" style="top:83px"><div class="n">03</div><div><b>TITLE GOES HERE</b><p>This is a sample text. You simply add your own text and description here. This text is fully editable.</p></div></div>
  <div class="g-item" style="top:109px"><div class="n">04</div><div><b>TITLE GOES HERE</b><p>This is a sample text. You simply add your own text and description here. This text is fully editable.</p></div></div>
  <div class="hub"><svg width="16" height="12" viewBox="0 0 16 12"><path d="M4 9H3a2.5 2.5 0 010-5 4 4 0 017.5-1A3 3 0 0113 9h-1" fill="none" stroke="#e0b13c" stroke-width="1"/><path d="M8 5v6M6 9l2 2 2-2" fill="none" stroke="#e0b13c" stroke-width="1"/></svg></div>
</section>

<!-- Interior -->
<section class="slide interior">
  <div class="photo" role="img" aria-label="Photo of a bright living room interior"></div>
  <div class="band"></div>
  <h2 class="abs h-gold">TITLE HERE</h2>
  <p class="abs tiny para">There are many variations of passages of lorem ipsum available, but the majority have suffered alteration in some form, by injected humour. There are many variations of passages of lorem ipsum available, but the majority have suffered alteration in some form, by injected humour.</p>
  <div class="col" style="left:132px"><b>Insert title here</b><p class="tiny">There are many variations of passages of lorem ipsum available, but the majority have suffered alteration in some form, by injected humour. There are many variations of passages of lorem ipsum available, but the majority</p></div>
  <div class="col" style="left:207px"><b>Insert title here</b><p class="tiny">There are many variations of passages of lorem ipsum available, but the majority have suffered alteration in some form, by injected humour. There are many variations of passages of lorem ipsum available, but the majority</p></div>
</section>

<!-- Two cards over team photo -->
<section class="slide duo">
  <div class="photo" role="img" aria-label="Photo of colleagues working together at a table"></div>
  <div class="duo-card" style="left:25px"><div class="top">Insert title here</div><p>There are many variations of passages of lorem ipsum available, but the majority have suffered alteration in some form, by injected humour. There are many variations of passages of lorem ipsum available, but the majority There are many variations of passages of lorem ipsum available, but the majority</p></div>
  <div class="duo-card" style="left:152px"><div class="top">Insert title here</div><p>There are many variations of passages of lorem ipsum available, but the majority have suffered alteration in some form, by injected humour. There are many variations of passages of lorem ipsum available, but the majority There are many variations of passages of lorem ipsum available, but the majority</p></div>
  <p class="abs foot">There are many variations of passages of lorem ipsum available, but the majority There are many variations of passages of lorem ipsum available.</p>
</section>

<!-- Services -->
<section class="slide services">
  <h2 class="abs center h-gold">OUR SERVICES</h2>
  <div class="abs center sub">Type the subtitle of your great here</div>
  <div class="stat-card">
    <div class="y">2023<span>/ November</span></div>
    <div class="s">Insert your amazing<br>statement here.</div>
    <svg width="52" height="44" viewBox="0 0 52 44" style="margin-top:6px">
      <g stroke="rgba(255,255,255,.45)" stroke-width="3" stroke-linecap="round">
        <path d="M6 4v32M13 4v32M20 4v32M27 4v32M34 4v32M41 4v32M48 4v32"/>
      </g>
      <g stroke="#fff" stroke-width="3" stroke-linecap="round">
        <path d="M6 16v20M13 10v26M20 22v14M27 8v28M34 18v18M41 12v24M48 6v30"/>
      </g>
      <g fill="#fff" font-size="2.4" font-family="Roboto,Arial,sans-serif" text-anchor="middle"><text x="6" y="42">Mon</text><text x="13" y="42">Tue</text><text x="20" y="42">Wed</text><text x="27" y="42">Thu</text><text x="34" y="42">Fri</text><text x="41" y="42">Sat</text><text x="48" y="42">Sun</text></g>
    </svg>
  </div>
  <div class="arrow">›</div>
  <div class="srv boxed"><div class="n">01</div><div><b>Insert title here</b><p>There are many variations of passages of lorem ipsum available, but the majority have suffered alteration in some form, by injected humour.</p></div></div>
  <div class="srv" style="left:137px;top:86px"><div class="n">02</div><div><b>Insert title here</b><p style="width:92px">There are many variations of passages of lorem ipsum available, but the majority have suffered alteration in some form, by injected humour.</p></div></div>
  <div class="srv" style="left:137px;top:116px"><div class="n">03</div><div><b>Insert title here</b><p style="width:92px">There are many variations of passages of lorem ipsum available, but the majority have suffered alteration in some form, by injected humour.</p></div></div>
</section>

<!-- Meet our team -->
<section class="slide team">
  <h2 class="abs center h-gold">MEET OUR TEAM</h2>
  <div class="abs center sub">Enter your subhead line here</div>
  <div class="member" style="left:12px"><div class="frame"><div class="g"></div><div class="p"></div><div class="name">NORA ELLIS</div><div class="pos">Position Text Holder</div></div><div class="social"><i></i><i></i><i></i></div></div>
  <div class="member" style="left:105px"><div class="frame"><div class="g"></div><div class="p"></div><div class="name">LIAM CARTER</div><div class="pos">Position Text Holder</div></div><div class="social"><i></i><i></i><i></i></div></div>
  <div class="member" style="left:198px"><div class="frame"><div class="g"></div><div class="p"></div><div class="name">NORA ELLIS</div><div class="pos">Position Text Holder</div></div><div class="social"><i></i><i></i><i></i></div></div>
</section>

<!-- Chart -->
<section class="slide chart">
  <h2 class="abs center h-gold">CHART INFOGRAPHIC</h2>
  <div class="abs center sub">Type the subtitle of your great here</div>
  <svg class="abs" style="left:28px;top:42px" width="225" height="96" viewBox="0 0 225 96" font-family="Roboto,Arial,sans-serif">
    <g stroke="#e3e3e3" stroke-width=".4">
      <path d="M14 4h200M14 11.5h200M14 19h200M14 26.5h200M14 34h200M14 41.5h200M14 49h200M14 56.5h200M14 64h200M14 71.5h200M14 79h200"/>
    </g>
    <g fill="#555" font-size="3" text-anchor="end">
      <text x="10" y="5">5</text><text x="10" y="12.5">4,5</text><text x="10" y="20">4</text><text x="10" y="27.5">3,5</text><text x="10" y="35">3</text><text x="10" y="42.5">2,5</text><text x="10" y="50">2</text><text x="10" y="57.5">1,5</text><text x="10" y="65">1</text><text x="10" y="72.5">0,5</text><text x="10" y="80">0</text>
    </g>
    <!-- bars: value * 15 px -->
    <g>
      <rect x="22" y="11.5" width="11" height="67.5" fill="var(--teal)"/>
      <rect x="34" y="43" width="11" height="36" fill="var(--gold)"/>
      <rect x="46" y="47.5" width="11" height="31.5" fill="var(--ink)"/>
      <rect x="70" y="41.5" width="11" height="37.5" fill="var(--teal)"/>
      <rect x="82" y="13" width="11" height="66" fill="var(--gold)"/>
      <rect x="94" y="47.5" width="11" height="31.5" fill="var(--ink)"/>
      <rect x="118" y="25" width="11" height="54" fill="var(--teal)"/>
      <rect x="130" y="52" width="11" height="27" fill="var(--gold)"/>
      <rect x="142" y="32.5" width="11" height="46.5" fill="var(--ink)"/>
      <rect x="166" y="10" width="11" height="69" fill="var(--teal)"/>
      <rect x="178" y="37" width="11" height="42" fill="var(--gold)"/>
      <rect x="190" y="2.5" width="11" height="76.5" fill="var(--ink)"/>
    </g>
    <path d="M14 79h200" stroke="#bbb" stroke-width=".5"/>
    <g fill="#555" font-size="3" text-anchor="middle">
      <text x="40" y="85">Term 1</text><text x="88" y="85">Term 2</text><text x="136" y="85">Term 3</text><text x="184" y="85">Term 4</text>
    </g>
    <g font-size="2.8" fill="#555">
      <rect x="90" y="90" width="2.5" height="2.5" fill="var(--teal)"/><text x="94" y="92.5">Title 1</text>
      <rect x="104" y="90" width="2.5" height="2.5" fill="var(--gold)"/><text x="108" y="92.5">Title 2</text>
      <rect x="118" y="90" width="2.5" height="2.5" fill="var(--ink)"/><text x="122" y="92.5">Title 3</text>
    </g>
  </svg>
  <div class="abs foot-bar"></div>
  <div class="abs foot">There are many variations of passages of lorem ipsum available, but the majority have suffered alteration in some form.</div>
  <div class="abs page">11</div>
</section>

<!-- Table -->
<section class="slide table-slide">
  <h2 class="abs center h-gold">TABLE</h2>
  <div class="abs center sub">Type the subtitle of your great here</div>
  <table class="data">
    <thead>
      <tr><th rowspan="2" style="width:52px">Task</th><th colspan="3">Risks</th><th colspan="2">Open</th><th rowspan="2" style="font-size:2.6px">Pending action</th></tr>
      <tr><th>High</th><th>Medium</th><th>Low</th><th>Issues</th><th>revisions</th></tr>
    </thead>
    <tbody>
      <tr><td>Task 01</td><td>21</td><td>21</td><td>21</td><td>21</td><td>21</td><td>21</td></tr>
      <tr><td>Task 02</td><td>55</td><td>55</td><td>55</td><td>55</td><td>55</td><td>55</td></tr>
      <tr><td>Task 03</td><td>45</td><td>45</td><td>45</td><td>45</td><td>45</td><td>45</td></tr>
      <tr><td>Task 04</td><td>86</td><td>86</td><td>86</td><td>86</td><td>86</td><td>86</td></tr>
      <tr><td>Task 05</td><td>21</td><td>21</td><td>21</td><td>21</td><td>21</td><td>21</td></tr>
      <tr><td>Task 06</td><td>45</td><td>45</td><td>45</td><td>45</td><td>45</td><td>45</td></tr>
      <tr><td>Task 07</td><td>63</td><td>63</td><td>63</td><td>63</td><td>63</td><td>63</td></tr>
      <tr><td>Task 08</td><td>75</td><td>75</td><td>75</td><td>75</td><td>75</td><td>75</td></tr>
      <tr><td>Task 09</td><td>85</td><td>85</td><td>85</td><td>85</td><td>85</td><td>85</td></tr>
      <tr><td>Task 10</td><td>21</td><td>21</td><td>21</td><td>21</td><td>21</td><td>21</td></tr>
      <tr><td>Total</td><td>/</td><td>/</td><td>/</td><td>/</td><td>/</td><td>/</td></tr>
    </tbody>
  </table>
</section>

<!-- Break section -->
<section class="slide break">
  <div class="photo" role="img" aria-label="Photo of a modern villa with a pool"></div>
  <div class="line" style="top:42px"></div>
  <h2 class="abs center">BREAK SECTION SLIDE</h2>
</section>

<!-- Q&A -->
<section class="slide qa">
  <div class="abs map" role="img" aria-label="Faint dotted world map"></div>
  <div class="abs center mark" style="text-align:center">Q&amp;A</div>
  <div class="abs center q" style="text-align:center">Do you have any question?<br>Feel free to ask.</div>
</section>

<!-- Contact -->
<section class="slide contact">
  <div class="abs center brand" style="text-align:center">Cobalt Lending</div>
  <div class="row">
    <span><svg width="9" height="11" viewBox="0 0 9 11"><path d="M4.5 10.5S1 6.5 1 4a3.5 3.5 0 017 0c0 2.5-3.5 6.5-3.5 6.5z" fill="none" stroke="#2e2b6e" stroke-width="1.2"/><circle cx="4.5" cy="4" r="1.2" fill="#2e2b6e"/></svg>Company Location, Address</span>
    <span><svg width="7" height="11" viewBox="0 0 7 11"><rect x=".7" y=".7" width="5.6" height="9.6" rx="1" fill="none" stroke="#2e2b6e" stroke-width="1.1"/><circle cx="3.5" cy="8.6" r=".6" fill="#2e2b6e"/></svg>+1 555 010 2470</span>
    <span><svg width="10" height="10" viewBox="0 0 10 10"><circle cx="5" cy="5" r="1.8" fill="none" stroke="#2e2b6e" stroke-width="1"/><path d="M6.8 5v1a1.3 1.3 0 002.6 0V5A4.4 4.4 0 105 9.4" fill="none" stroke="#2e2b6e" stroke-width="1"/></svg>info@yourwebsite.com</span>
    <span><svg width="10" height="10" viewBox="0 0 10 10"><circle cx="5" cy="5" r="4.3" fill="none" stroke="#2e2b6e" stroke-width="1"/><ellipse cx="5" cy="5" rx="1.8" ry="4.3" fill="none" stroke="#2e2b6e" stroke-width=".7"/><path d="M.7 5h8.6" stroke="#2e2b6e" stroke-width=".7"/></svg>www.yourwebsite.com</span>
  </div>
  <div class="abs center url" style="text-align:center">https://www.cobaltlending.com/</div>
  <div class="social"><i></i><i></i><i></i><i></i><i></i><i></i></div>
  <div class="photo" role="img" aria-label="Photo of a modern white villa exterior"></div>
</section>

</body>
</html>
```